Cardiology practice business card

We need a business card for our cardiology practice "Wattle Cardiology". We have a new logo, attached below. We like the colours in the logo - red and charcoal. The front of the business card will need to have the doctors name, address, phone number and email. The back will need to have space to write 2 appointment dates and times.

```html
<!DOCTYPE html>
<html lang="en">
<head>
<meta charset="utf-8">
<title>Wattle Cardiology – Business Card</title>
<link rel="stylesheet" href="https://fonts.googleapis.com/css2?family=Poppins:wght@300;400;500;600;700&display=swap">
<style>
  :root {
    --red: #ec2027;
    --charcoal: #54575a;
    --ink: #111111;
    --grey-text: #5f6163;
    --white: #ffffff;
    --backdrop: #cfd3d3;
    --rule: #c9cbcc;
  }
  * { box-sizing: border-box; margin: 0; padding: 0; }
  html, body { width: 1200px; height: 960px; overflow: hidden; }
  body {
    background: var(--backdrop);
    font-family: "Poppins", sans-serif;
    position: relative;
  }
  .card {
    position: absolute;
    left: 249px;
    width: 701px;
    height: 400px;
    border-radius: 26px;
    overflow: hidden;
  }

  /* Back: appointment side */
  .card-back { top: 60px; background: var(--charcoal); color: var(--white); }
  .back-brand {
    position: absolute; top: 44px; left: 0; right: 0;
    text-align: center;
    font-size: 26px; font-weight: 500; letter-spacing: 2px;
    text-transform: uppercase; color: var(--white);
  }
  .back-title {
    position: absolute; top: 94px; left: 0; right: 0;
    text-align: center; font-size: 27px; font-weight: 400;
  }
  .appointment {
    position: absolute; left: 25px; width: 650px; height: 114px;
    background: var(--red); border-radius: 7px; padding: 0 3px 3px;
  }
  .appointment.first { top: 137px; }
  .appointment.second { top: 261px; }
  .weekdays {
    display: flex; justify-content: space-between;
    height: 36px; align-items: center;
    padding: 0 15px 0 16px;
    font-size: 19px; font-weight: 400; color: var(--white);
  }
  .fields {
    background: var(--white); border-radius: 5px;
    height: 75px; padding: 8px 12px 0 10px; color: var(--ink);
  }
  .field-row { display: flex; align-items: baseline; font-size: 19px; height: 35px; }
  .field-row .label { white-space: nowrap; }
  .field-row .blank {
    flex: 1; border-bottom: 1px dashed #333; margin: 0 4px; transform: translateY(-4px);
  }
  .field-row .blank.short { flex: 0 0 115px; margin-right: 0; }

  /* Front: contact side */
  .card-front { top: 500px; background: var(--white); }
  .front-brand {
    position: absolute; top: 44px; left: 30px;
    display: flex; align-items: center; gap: 14px;
  }
  .brand-dot { width: 22px; height: 22px; border-radius: 50%; background: var(--red); }
  .brand-name {
    font-size: 34px; font-weight: 600; line-height: 1.15;
    text-transform: uppercase; letter-spacing: 2px; color: var(--charcoal);
  }
  .person { position: absolute; top: 160px; right: 27px; text-align: right; }
  .person-name {
    font-size: 39px; line-height: 1.1; padding-bottom: 2px;
    border-bottom: 1px solid var(--rule);
  }
  .person-name .given { color: var(--red); font-weight: 600; }
  .person-name .family { color: var(--grey-text); font-weight: 300; }
  .person-role { font-size: 19px; font-weight: 600; color: var(--ink); margin-top: 3px; }
  .accent-bar {
    position: absolute; right: 0; top: 169px; width: 20px; height: 61px; background: var(--red);
  }
  .address {
    position: absolute; left: 25px; top: 226px;
    font-size: 19.5px; line-height: 26px; color: var(--red);
  }
  .contacts { position: absolute; left: 25px; top: 298px; list-style: none; }
  .contacts li {
    display: flex; align-items: center; gap: 12px;
    font-size: 20px; line-height: 26px; color: var(--ink);
  }
  .contacts svg { width: 17px; height: 17px; fill: var(--red); flex: none; }
</style>
</head>
<body>

<section class="card card-back">
  <div class="back-brand">Wattle Cardiology</div>
  <h2 class="back-title">Appointment</h2>

  <div class="appointment first">
    <div class="weekdays"><span>Sun</span><span>Mon</span><span>Tue</span><span>Wed</span><span>Thr</span><span>Fri</span><span>Sat</span></div>
    <div class="fields">
      <div class="field-row"><span class="label">Date/Month</span><span class="blank"></span></div>
      <div class="field-row"><span class="label">Time</span><span class="blank"></span><span class="label">Year</span><span class="blank short"></span></div>
    </div>
  </div>

  <div class="appointment second">
    <div class="weekdays"><span>Sun</span><span>Mon</span><span>Tue</span><span>Wed</span><span>Thr</span><span>Fri</span><span>Sat</span></div>
    <div class="fields">
      <div class="field-row"><span class="label">Date/Month</span><span class="blank"></span></div>
      <div class="field-row"><span class="label">Time</span><span class="blank"></span><span class="label">Year</span><span class="blank short"></span></div>
    </div>
  </div>
</section>

<section class="card card-front">
  <div class="front-brand">
    <span class="brand-dot"></span>
    <div class="brand-name">Wattle<br>Cardiology</div>
  </div>

  <div class="person">
    <div class="person-name"><span class="given">Maren</span> <span class="family">Dovack</span></div>
    <div class="person-role">Founder &amp; CEO</div>
  </div>
  <div class="accent-bar"></div>

  <address class="address" style="font-style:normal">
    418 Ridgeline Ave. Suite 120<br>
    Millbrook, TX 75390
  </address>

  <ul class="contacts">
    <li>
      <svg viewBox="0 0 24 24" aria-hidden="true"><path d="M6.6 10.8a15.1 15.1 0 0 0 6.6 6.6l2.2-2.2c.3-.3.7-.4 1-.2 1.1.4 2.3.6 3.6.6.6 0 1 .4 1 1V20c0 .6-.4 1-1 1A17 17 0 0 1 3 4c0-.6.4-1 1-1h3.5c.6 0 1 .4 1 1 0 1.3.2 2.5.6 3.6.1.3 0 .7-.2 1z"/></svg>
      <span>(555) 014-7263</span>
    </li>
    <li>
      <svg viewBox="0 0 24 24" aria-hidden="true"><path d="M12 2a10 10 0 1 0 0 20 10 10 0 0 0 0-20zm-1 17.9A8 8 0 0 1 4.1 10L9 15v1a2 2 0 0 0 2 2zm6.9-2.5A2 2 0 0 0 16 16h-1v-3a1 1 0 0 0-1-1H8v-2h2a1 1 0 0 0 1-1V7h2a2 2 0 0 0 2-2v-.4a8 8 0 0 1 2.9 12.8z"/></svg>
      <span>www.wattlecardiology.com</span>
    </li>
    <li>
      <svg viewBox="0 0 24 24" aria-hidden="true"><path d="M2 9l10-7 10 7v12H2zm2 2v8h16v-8l-8 5z"/></svg>
      <span>hello@wattlecardiology.com</span>
    </li>
  </ul>
</section>

</body>
</html>
```